Homepage Design for Digital Advertising Company

The website will be very simple, with just one page (the homepage).

We are a new startup company, Brightlane Media, and focus on social media and gaming advertising. We work directly with brands, and with other media agencies. I have attached some details about our company, what we do, and content you can use for the website. I have also attached a screenshot of our logo (high quality files will be provided shortly).

This is an example of a website we really like. They do not do what we do, however their layout is great, and the best part about it is that they really get the message accross of exactly what they do as soon as the page loads. We do not have a product video, so that part does not apply, however i love their basic page layout.
http://www.vorelqin.com/

We can say something like this:
Simple Social Media and Gaming Advertising (BIG TEXT)
WE DELIVER: Plumbook fans and likes, Chirpel followers, Targeted ads and video, and more... (SubText)

On the homepage, we want to have a prominent "Free Consultation" box with a "Submit" button. This box will have input boxes for:
Name
Email
Phone
Or, we can do just a simple email submit as seen here (I like how they did a one long page design BTW)
http://mornivex.com/

Here are some other sites i like:
http://www.tabrolin.com/
http://www.kelvaro.com/
http://graystitch.net/

Not sure what you will get out of this one, but its too unique to not mention:
http://yulomar.com/handset/

COLORS:
We are flexible on color scheme. We can change the color of the logo, so dont let that limit your color concepts.

Content on site:
We can use fly out buttons or "more" links for extra text dropdowns if you only want to include an excerpt from each topic in the attached content sheet. Dont want page to be too busy.

Long One Page:
We are not opposed to something like this, by the way
http://mornivex.com/

Target Market(s)

big brands, advertising agencies

Industry/Entity Type

Digital

Requirements
Must have
• Logo
Sign up form
Nice to have
• all the content from our attachment
Should not have
• busy designs, lack of white space, too much text

```html
<!DOCTYPE html>
<html lang="en">
<head>
<meta charset="utf-8">
<title>Brightlane Media</title>
<link href="https://fonts.googleapis.com/css2?family=Open+Sans:wght@400;600;700&family=Arimo:wght@400;700&family=Marcellus&display=swap" rel="stylesheet">
<style>
:root{
  --blue:#1a73c0;
  --blue-dark:#0d4f96;
  --ink:#333;
  --muted:#555;
  --hero-top:#dbe9ec;
  --hero-bot:#a9c3ca;
  --orange:#f39a37;
  --line:#d5d9dc;
  --card:#fafafa;
}
*{box-sizing:border-box;margin:0;padding:0}
html,body{width:1200px;height:1173px;overflow:hidden;background:#fff}
body{position:relative;font-family:Arimo,Arial,sans-serif;color:var(--ink)}
.abs{position:absolute}

.topnav{left:0;top:0;width:1200px;height:45px;border-top:4px solid var(--blue-dark);background:linear-gradient(#fff,#e8eef0);border-bottom:1px solid #c9d4d8}
.topnav ul{list-style:none;position:absolute;left:149px;top:7px;display:flex;gap:0}
.topnav li{font:600 13px "Open Sans",sans-serif;padding:5px 16px;margin-right:6px;color:#222}
.topnav li.active{border:1px solid #aab;border-radius:4px;background:#fff;box-shadow:0 1px 2px rgba(0,0,0,.2)}
.callnum{right:127px;top:8px;font:400 23px "Open Sans",sans-serif;color:#555;display:flex;align-items:center;gap:8px}
.callnum b{font-weight:700;color:#444}

.hero{left:0;top:45px;width:1200px;height:429px;background:linear-gradient(var(--hero-top),var(--hero-bot))}
.brand{left:152px;top:50px;font:400 27px "Open Sans",sans-serif;color:#333;display:flex;align-items:center;gap:8px}
.brand i{display:block;width:14px;height:14px;border-radius:50%;background:var(--blue)}
.headline{left:154px;top:106px;width:460px;font:700 24px/30px "Open Sans",sans-serif;color:#333}
.headline em{font-style:normal;color:var(--blue)}
.headline strong{color:#111}
.mascot{left:515px;top:138px;width:46px;height:72px;border-radius:20px;background:linear-gradient(#f7b04a,#e4822a)}
.hero hr{position:absolute;left:154px;top:212px;width:437px;border:0;border-top:1px solid #b9cbd0}
.points{left:154px;top:228px;list-style:none;font-size:12px;letter-spacing:.5px;color:#222}
.points li{height:23px;display:flex;align-items:center;gap:8px}
.points li::before{content:"";width:0;height:0;border-top:5px solid transparent;border-bottom:5px solid transparent;border-right:6px solid var(--blue-dark)}
.btn{border-radius:6px;font:400 15px "Open Sans",sans-serif;display:flex;align-items:center;justify-content:center}
.btn-blue{left:155px;top:388px;width:160px;height:41px;background:linear-gradient(#3b9be4,#1667b8);color:#fff;border:2px solid #fff;box-shadow:0 1px 3px rgba(0,0,0,.3)}
.btn-grey{left:345px;top:386px;width:116px;height:44px;background:linear-gradient(#fff,#e0e0e0);color:#333;border:1px solid #bbb}
.shot{left:656px;top:85px;width:402px;height:340px;background:linear-gradient(#fdfdfd,#e9ecee);border:4px solid #fff;box-shadow:0 6px 18px rgba(0,0,0,.2);transform:perspective(900px) rotateY(-12deg)}
.dots{left:907px;top:428px;display:flex;gap:11px}
.dots span{width:18px;height:18px;border-radius:50%;background:var(--orange);border:2px solid #fff}
.dots span.on{background:var(--blue)}

.card{top:514px;width:290px;height:246px;background:linear-gradient(#fff,var(--card));border-top:5px solid var(--blue);border-radius:8px 8px 10px 10px;box-shadow:0 1px 4px rgba(0,0,0,.15)}
.card::after{content:"";position:absolute;left:30px;right:30px;bottom:-14px;height:8px;border-radius:50%;background:rgba(0,0,0,.12);filter:blur(3px)}
.card h2{position:absolute;left:12px;top:14px;font:400 21px Marcellus,serif;color:var(--blue);padding-bottom:8px;border-bottom:1px dotted #aaa}
.card p{position:absolute;left:10px;top:62px;width:266px;font-size:12px;line-height:19.2px;color:var(--muted);letter-spacing:.3px}
.card p b{color:#333}
.c1{left:135px}.c2{left:449px}.c3{left:764px}
.c2 p{text-align:justify;left:14px;width:266px}
.team{left:32px;top:120px;width:220px;height:118px;border-radius:8px;background:linear-gradient(#e2e6e8,#f4f6f7)}
.form label{position:absolute;left:22px;font-size:13px;color:#444}
.form .field{position:absolute;left:76px;width:206px;height:27px;border:1px solid #cdd;border-radius:14px;background:linear-gradient(#f2f4f5,#fff);box-shadow:inset 0 1px 2px rgba(0,0,0,.1)}
.submit{position:absolute;left:187px;top:186px;width:84px;height:30px;border-radius:6px;background:linear-gradient(#2b8ee0,#0c5fae);color:#fff;font:700 13px "Open Sans",sans-serif;display:flex;align-items:center;justify-content:center;letter-spacing:.5px;border:1px solid #0b4f92}

.touch{left:154px;top:820px;width:892px;height:134px;background:linear-gradient(#fff,#eceeef);border-radius:4px}
.touch::after{content:"";position:absolute;left:30px;right:40px;bottom:-22px;height:10px;border-radius:50%;background:rgba(0,0,0,.12);filter:blur(4px)}
.sep{top:0;width:2px;height:130px;background:linear-gradient(transparent,#d0d4d6,transparent)}
.touch h3{position:absolute;left:21px;top:12px;font:400 20px "Open Sans",sans-serif;color:#333}
.talk{left:72px;top:38px;font-size:13px;line-height:17px}
.talk .k{color:var(--blue);font-size:12px}
.talk .t{font-size:14px;color:#222}
.talk .n{letter-spacing:1px;color:#333}
.mail{left:373px;top:50px;font-size:14px;letter-spacing:1px;line-height:20px;color:#333}
.social{left:604px;font-size:13px;letter-spacing:.6px;color:#333;display:flex;align-items:center;gap:12px}
.share{width:78px;height:26px;border-radius:2px;color:#fff;font-size:11px;display:flex;align-items:center;gap:7px;padding-left:6px}
.share i{width:14px;height:14px;background:rgba(255,255,255,.85);border-radius:2px}
.s-pb{background:linear-gradient(#5a78b4,#3b5998)}
.s-ch{background:linear-gradient(#8bd8f2,#4ab5de)}

.footer{left:0;top:986px;width:1200px;height:187px;background:linear-gradient(#e9ebec,#f8f8f8);border-top:1px solid #ccc}
.fcol{top:1008px;font-size:12px;line-height:23.5px;color:#555;letter-spacing:.4px}
.ficons{left:820px;top:1018px;display:flex;gap:20px;font-size:11px;color:#555;text-align:center}
.ficons div{width:40px;display:flex;flex-direction:column;align-items:center;gap:4px}
.ficons svg{width:26px;height:26px}
.bottomline{left:134px;top:1119px;width:930px;border-top:1px solid #ddd}
.legal{left:0;top:1139px;width:1200px;text-align:center;font-size:11px;color:#444}
.legal span{margin:0 6px}
</style>
</head>
<body>

<nav class="abs topnav">
  <ul>
    <li class="active">HOME</li><li>ABOUT US</li><li>FAQ</li><li>SUPPORT</li><li>TESTIMONIALS</li><li>BLOG</li>
  </ul>
</nav>
<div class="abs callnum">
  <svg width="30" height="30" viewBox="0 0 30 30"><circle cx="15" cy="15" r="13.5" fill="none" stroke="#444" stroke-width="2"/><path d="M10 8c-2 2-1 6 3 10s8 5 10 3l-3-3-2 1c-2-1-4-3-5-5l1-2z" fill="#444"/></svg>
  <span>Call: <b>1-555-204-7731</b></span>
</div>

<section class="abs hero">
  <div class="abs brand"><i></i>Brightlane Media</div>
  <h1 class="abs headline">As a media buyer, <em>it is extremely important to attract the most targeted audience</em> <strong>POSSIBLE</strong></h1>
  <div class="abs mascot" role="img" aria-label="Orange figure holding a megaphone"></div>
  <hr>
  <ul class="abs points">
    <li>Gamers are always seeking to conquer the next level in their game of choice.</li>
    <li>Banner ads can be placed in virtually any area on a social game.</li>
    <li>We are able to acquire Plumbook likes and Chirpel followers for your brand</li>
    <li>Integrating your brand with your customers' games offers the highest</li>
  </ul>
  <div class="abs btn btn-blue" style="top:343px">More info Click here</div>
  <div class="abs btn btn-grey" style="top:341px">Sing up Now</div>
  <div class="abs shot" style="top:40px" role="img" aria-label="Screenshot of a news search results page with headlines and retail photos"></div>
  <div class="abs dots" style="top:383px"><span class="on"></span><span></span><span></span><span></span><span></span></div>
</section>

<article class="abs card c1">
  <h2>How We Can Help:</h2>
  <p><b>As a media buyer, it is extremely important to attract the most targeted</b> audience possible while maximizing your</p>
  <div class="abs team" role="img" aria-label="Group of people in sportswear standing together"></div>
</article>

<article class="abs card c2">
  <h2>In Game Sponsorships:</h2>
  <p><b>Integrating your brand with your customers' games offers the highest</b> level of engagement possible in the digital media space. We can customize the game skin or interface to your brand logo and color to create constant brand awareness for the user.Another method of integration is to offer your actual product or service in the virtual gaming....</p>
</article>

<article class="abs card c3 form">
  <h2 style="width:200px">Free Consultation</h2>
  <label style="top:76px">Name :</label><span class="field" style="top:70px"></span>
  <label style="top:114px">Email :</label><span class="field" style="top:108px"></span>
  <label style="top:152px">Phone :</label><span class="field" style="top:146px"></span>
  <div class="submit">SUBMIT</div>
</article>

<section class="abs touch">
  <h3>Get in touch</h3>
  <svg class="abs" style="left:36px;top:40px" width="26" height="52" viewBox="0 0 26 52"><rect x="1" y="1" width="24" height="50" rx="5" fill="#222"/><rect x="4" y="8" width="18" height="32" fill="#7fa9cf"/><circle cx="13" cy="45" r="2.5" fill="#555"/></svg>
  <div class="abs talk"><div class="k">TALK TO US</div><div class="t">Phone</div><div class="n">(91) 55501-23874</div></div>
  <div class="abs sep" style="left:292px"></div>
  <svg class="abs" style="left:330px;top:46px" width="48" height="40" viewBox="0 0 48 40"><rect x="4" y="4" width="40" height="30" rx="3" fill="#3aa7d8"/><path d="M4 6l20 16 20-16" fill="none" stroke="#e8f6fc" stroke-width="2"/><circle cx="6" cy="20" r="5" fill="#f5b332"/></svg>
  <div class="abs mail">Email Address<br>info@brightlanemedia.com</div>
  <div class="abs sep" style="left:588px"></div>
  <div class="abs social" style="top:54px"><div class="share s-pb"><i></i>SHARE</div>Sign in with Plumbook.</div>
  <div class="abs social" style="top:94px"><div class="share s-ch"><i></i>SHARE</div>Sign in with Chirpel.</div>
</section>

<footer class="abs footer"></footer>
<div class="abs fcol" style="left:152px">Toll Free (NA): 1-555-318-4420<br>Toll Free (UK): 0800-555-0192<br>Toll Free (Ireland): 1-800-555-017<br>Phone: 416-555-0148</div>
<div class="abs fcol" style="left:372px">Toll Free (NA): 1-555-318-4420<br>Toll Free (UK): 0800-555-0192<br>Toll Free (Ireland): 1-800-555-017<br>Phone: 416-555-0148</div>
<div class="abs fcol" style="left:583px;top:1006px">Toll Free (NA): 1-555-318-4420<br>Toll Free (UK): 0800-555-0192<br>Toll Free (Ireland): 1-800-555-017<br>Phone: 416-555-0148</div>
<div class="abs ficons">
  <div><svg viewBox="0 0 26 26"><circle cx="5" cy="21" r="3" fill="#777"/><path d="M3 12a11 11 0 0 1 11 11M3 4a19 19 0 0 1 19 19" fill="none" stroke="#777" stroke-width="3.5"/></svg>Blog</div>
  <div><svg viewBox="0 0 26 26"><rect x="1" y="1" width="24" height="24" rx="3" fill="#777"/><path d="M10 7l9 6-9 6z" fill="#fff"/></svg>Streamly</div>
  <div><svg viewBox="0 0 26 26"><rect x="1" y="1" width="24" height="24" rx="4" fill="#777"/></svg>Plumbook</div>
  <div><svg viewBox="0 0 26 26"><circle cx="13" cy="13" r="11" fill="#777"/></svg>Chirpel</div>
</div>
<div class="abs bottomline"></div>
<div class="abs legal">©2012 Brightlane <span>·</span> About <span>·</span> Press <span>·</span> Careers <span>·</span> Terms <span>·</span> Privacy Policy <span>·</span> Support <span>·</span> Resources</div>

</body>
</html>
```